Renate Falkner
Heilpraktikerin eingeschränkt auf den Bereich der Psychotherapie
Ausbildungen:
Diplom Sozialpädagogin (FH)
Systemische Sucht- Paar- und Familientherapeutin
Schwerpunkte:
-Beratungen in Lebenskrisen
-Burn Out
-Suchttherapie
-Einzeltherapie
- Gruppentherapie
-Paartherapie
- Familientherapie
Arbeiten mit:
-Familienrekonstruktion
-Symbolen
-Skulpturen
-Empathie
-Verständnis
...Wir sollten heiter Raum um Raum durchschreiten und an keinem wie an einer Heimat hängen. Der Weltgeist will nicht fesseln und uns engen, er will uns Stuf um Stufe heben, weiten...
Wohlan denn Herz nimm Abschied und gesunde
(Gustav Lindner: "Wellen")

```html
<!DOCTYPE html>
<html lang="de">
<head>
<meta charset="utf-8">
<title>Renate Falkner – Heilpraktikerin</title>
<link rel="stylesheet" href="https://fonts.googleapis.com/css2?family=Jost:ital,wght@0,500;0,600;0,700;1,600&display=swap">
<style>
  :root {
    --page-bg: #ffffff;
    --front-red: #a8092b;
    --back-purple: #7e0a6e;
    --cream: #eee5d8;
    --lavender: #a996cc;
    --heading-lavender: #a392c8;
    --slate: #5c4a6e;
    --ink-dark: #1e1530;
    --text-dark: #2a1230;
  }
  * { margin: 0; padding: 0; box-sizing: border-box; }
  html, body { width: 1200px; height: 900px; overflow: hidden; background: var(--page-bg); }
  body { position: relative; font-family: "Jost", "Futura", sans-serif; }

  .flyer-page {
    position: absolute; top: 39px; width: 580px; height: 817px; overflow: hidden;
    box-shadow: 3px 4px 8px rgba(0,0,0,0.35);
  }
  .flyer-front { left: 12px; background: var(--front-red); }
  .flyer-back { left: 606px; background: var(--back-purple); }

  .front-title {
    position: absolute; left: 7px; top: 82px; font-weight: 600; font-size: 53px;
    letter-spacing: 0.5px; color: var(--heading-lavender); line-height: 1;
  }
  .front-name {
    position: absolute; right: 6px; top: 130px; font-weight: 700; font-size: 60px;
    color: var(--cream); line-height: 1; white-space: nowrap;
  }
  .front-circles, .back-graphic { position: absolute; left: 0; top: 0; }

  .front-quote {
    position: absolute; left: 0; width: 100%; top: 576px; text-align: center;
    color: var(--cream); font-weight: 600; font-size: 17.5px; line-height: 23.5px;
  }
  .front-quote-author {
    position: absolute; left: 0; width: 100%; top: 710px; text-align: center;
    color: var(--cream); font-weight: 600; font-style: italic; font-size: 17.5px;
  }

  .back-heading {
    position: absolute; left: 0; width: 100%; top: 52px; text-align: center;
    color: var(--cream); font-weight: 600; line-height: 1.2;
  }
  .back-heading-degree { font-size: 28px; }
  .back-heading-training { font-size: 20px; margin-top: 4px; }

  .back-graphic text { font-family: "Jost", "Futura", sans-serif; font-weight: 600; }
  .focus-small { font-size: 19px; font-weight: 700; fill: var(--text-dark); }
  .focus-large { font-size: 26px; font-weight: 700; fill: var(--text-dark); }
  .focus-burnout { font-size: 43px; font-weight: 700; fill: var(--text-dark); }
  .method-word { font-size: 18px; font-weight: 700; fill: var(--lavender); }

  .back-contact {
    position: absolute; left: 0; width: 100%; top: 640px; text-align: center;
    color: var(--cream); font-weight: 600; font-size: 17.5px; line-height: 23px;
    font-style: normal;
  }
</style>
</head>
<body>
  <section class="flyer-page flyer-front">
    <h1 class="front-title">HEILPRAKTIKERIN</h1>
    <p class="front-name">RENATE FALKNER</p>
    <svg class="front-circles" width="580" height="817" viewBox="0 0 580 817" aria-hidden="true">
      <circle cx="288" cy="234" r="20" fill="var(--ink-dark)" stroke="#6b0a22" stroke-width="1.5"/>
      <circle cx="288" cy="296" r="27" fill="var(--slate)" stroke="#6b0a22" stroke-width="1.5"/>
      <circle cx="288" cy="373" r="37" fill="var(--lavender)" stroke="#6b0a22" stroke-width="1.5"/>
      <circle cx="288" cy="484" r="59" fill="var(--cream)" stroke="#6b0a22" stroke-width="1.5"/>
    </svg>
    <p class="front-quote">
      Wir wollen ruhig Weg um Weg beschreiten,<br>
      an keinem Ort zu lange stehen bleiben,<br>
      das Leben will uns nicht zum Stillstand treiben,<br>
      es will uns Well' um Welle tragen, weiten!<br>
      So geh denn, Herz, und lerne neu zu blühen!
    </p>
    <p class="front-quote-author">Gustav Lindner</p>
  </section>

  <section class="flyer-page flyer-back">
    <div class="back-heading">
      <h2 class="back-heading-degree">Diplom Sozialpädagogin</h2>
      <p class="back-heading-training">Systemische Sucht- Paar- und Familientherapeutin</p>
    </div>
    <svg class="back-graphic" width="580" height="817" viewBox="0 0 580 817" aria-hidden="true">
      <circle cx="294" cy="380" r="59" fill="var(--cream)" stroke="#4e0645" stroke-width="1.5"/>
      <circle cx="194" cy="445" r="38" fill="var(--lavender)" stroke="#4e0645" stroke-width="1.5"/>
      <circle cx="181" cy="530" r="26" fill="var(--slate)" stroke="#4e0645" stroke-width="1.5"/>
      <circle cx="205" cy="597" r="20" fill="var(--ink-dark)" stroke="#4e0645" stroke-width="1.5"/>

      <text class="focus-small" transform="translate(192 210) rotate(58)">Einzeltherapie</text>
      <text class="focus-small" transform="translate(120 246) rotate(32)">Gruppentherapie</text>
      <text class="focus-small" transform="translate(117 326) rotate(12)">Paartherapie</text>
      <text class="focus-small" transform="translate(77 400) rotate(-8)">Familientherapie</text>

      <text class="focus-burnout" transform="translate(348 346) rotate(-30)">Burn Out</text>
      <text class="focus-large" transform="translate(358 381) rotate(-10)">Suchttherapie</text>
      <text class="focus-large" transform="translate(357 407) rotate(20)">Beratungen in</text>
      <text class="focus-large" transform="translate(352 439) rotate(20)">Lebenskrisen</text>

      <text class="method-word" transform="translate(202 511) rotate(-35)">Symbole</text>
      <text class="method-word" transform="translate(214 530) rotate(-15)">Skulpturen</text>
      <text class="method-word" transform="translate(216 552) rotate(5)">Empathie</text>
    </svg>
    <address class="back-contact">
      Renate Falkner<br>
      Lindenweg 12c , 82340 Feldkirchen<br>
      Telefon: 08152/555 20 40 ,Mobil: 0171/ 5550123<br>
      e-Mail: renate.falkner@posteck.de
    </address>
  </section>
</body>
</html>
```